Postcard for Antique Furniture Restorer

My business is to restore antique furniture. I am based in Sydney, Australia.

I will be using this postcard to promote my business.
I will give it to customers like a With Compliments card.

Sometimes I will be writing information on the back of the card.

Design for Postcard Size eg 148 X 105mm

Front of card:

Attached are images of Antique furniture - please use ONLY 1 of the 3 images.
Deep etch the image on a white or cream background.

On front of card add these words:
Timber Reborn
antique furniture restoration

Antiques travel through time, seeing generations of families
Through time they remain - they tell a continuing story
Be part of the journey

Back of postcard:
(leave space for notes to be handwritten)

Add these words:

Timber Reborn
Corin Maddox
mobile 0437 552 618
www.oakandvarnishcraft.com.au

Industry/Entity Type

Business

Font styles to use
Serif
Sans Serif

Colors
fefdec
ffffff

Requirements
Must have
• Use only 1 image. Image must be deep etched.

```html
<!DOCTYPE html>
<html lang="en">
<head>
<meta charset="utf-8">
<title>Timber Reborn – Postcard</title>
<link rel="stylesheet" href="https://fonts.googleapis.com/css2?family=Cabin:wght@600;700&family=Crimson+Text:ital,wght@0,400;0,700;1,400&display=swap">
<style>
  :root {
    --stage: #7a7a7a;
    --ink: #5a2a12;
    --ink-soft: #6b3a1e;
    --front-light: #ecdcb9;
    --front-mid: #d9bf8e;
    --front-edge: #8a5a2a;
    --back-light: #f5efe4;
    --back-mid: #ece2d0;
    --wood-light: #b5532c;
    --wood-dark: #4a1a0c;
  }
  * { margin: 0; padding: 0; box-sizing: border-box; }
  html, body { width: 1200px; height: 534px; overflow: hidden; }
  body { background: var(--stage); position: relative; font-family: "Crimson Text", Georgia, serif; color: var(--ink); }

  .card { position: absolute; top: 56px; width: 556px; height: 398px; }
  .card--front {
    left: 36px;
    background:
      linear-gradient(180deg, transparent 78%, var(--front-mid) 90%, var(--front-edge) 100%),
      radial-gradient(ellipse at 30% 40%, var(--front-light) 0%, var(--front-mid) 100%);
  }
  .card--back {
    left: 610px;
    background: radial-gradient(ellipse at 40% 40%, var(--back-light) 0%, var(--back-mid) 100%);
  }

  .brand { position: absolute; width: 320px; text-align: center; font-family: "Cabin", Arial, sans-serif; }
  .brand__name { font-size: 22px; font-weight: 700; line-height: 1; }
  .brand__tagline { font-size: 16.5px; font-weight: 700; line-height: 1; margin-top: 7px; }
  .card--front .brand { left: 0; top: 82px; }
  .card--back .brand { left: -6px; top: 128px; }

  .story { position: absolute; left: 0; top: 156px; width: 320px; text-align: center; }
  .story__line { font-style: italic; font-size: 14px; line-height: 19.5px; color: var(--ink-soft); }
  .story__call { font-size: 15px; line-height: 19px; margin-top: 4px; color: var(--ink-soft); }

  .piece-image {
    position: absolute; left: 300px; top: 26px; width: 222px; height: 320px;
    background: linear-gradient(90deg, var(--wood-dark) 0%, var(--wood-light) 35%, var(--wood-dark) 50%, var(--wood-light) 70%, var(--wood-dark) 100%);
  }

  .contact { position: absolute; left: -6px; top: 198px; width: 320px; text-align: center; }
  .contact__name { font-style: italic; font-size: 18px; line-height: 24px; color: var(--ink-soft); }
  .contact__phone { font-weight: 700; font-size: 17px; line-height: 24px; }
  .contact__web { font-weight: 700; font-size: 12px; line-height: 20px; }
</style>
</head>
<body>
  <section class="card card--front">
    <div class="brand">
      <p class="brand__name">Timber Reborn</p>
      <p class="brand__tagline">Antique Furniture Restoration</p>
    </div>
    <div class="story">
      <p class="story__line">Antiques travel through time, seeing<br>generations of families</p>
      <p class="story__line">Through time they remain - they tell a<br>continuing story</p>
      <p class="story__call">Be part of the journey</p>
    </div>
    <div class="piece-image" role="img" aria-label="Deep-etched photograph of a carved antique burl-wood armoire"></div>
  </section>

  <section class="card card--back">
    <div class="brand">
      <p class="brand__name">Timber Reborn</p>
      <p class="brand__tagline">Antique Furniture Restoration</p>
    </div>
    <div class="contact">
      <p class="contact__name">Corin Maddox</p>
      <p class="contact__phone">0437 552 618</p>
      <p class="contact__web">www.oakandvarnishcraft.com.au</p>
    </div>
  </section>
</body>
</html>
```